Plakat für Tanzschule
Zielgruppe
Wir sind eine Tanzschule
Hallo,
ich benötige ein professionelles Design für ein Schild im Format 2 Meter breit × 1 Meter hoch (Querformat), das von einem stark frequentierten Parkplatz aus gut sichtbar ist.
✅ Ziel:
Gestaltung eines aufmerksamkeitsstarken, eleganten und energiegeladenen Werbeschilds
Das Schild soll sofort zeigen, worum es geht (Tanzstile) und zum kostenlosen Schnuppern motivieren
Die Gestaltung soll hochwertig und grafisch modern wirken
Bild / Hintergrund:
Ich habe einen ersten Design-Vorschlag hochgeladen (Screenshot)
⚠️ Ursprünglich hatte ich vor, ein bereits ausgeschnittenes und bearbeitetes Bild zu liefern (z. B. Unreinheiten und Störungen im Bild zu glätten oder zu entfernt und Zähne etwas weißer). Das kann ich jetzt leider doch nicht nachreichen. Daher müsste doch die Bearbeitung des Bildes mit übernommen werden.
✏️ Textinhalte (hierarchisch sortiert):
TANZSCHULE
Salsa · Bachata · Kizomba · Zouk
Jetzt Gratis Schnuppern!
Ritmo y Alma (Markenname)
www.ritmo-y-alma.de
???? Wichtig:
Die wichtigsten Inhalte (Tanzarten & CTA) müssen sofort erfassbar sein
Design bitte auf Fernwirkung, klare Lesbarkeit und modernes visuelles Layout ausrichten
Text in sinnvollen Größenabstufungen und mit sauberer visueller Hierarchie
Unsere eigentliche Hauptfarbe ist #ad194f, bis jetzt habe ich aber noch keine schöne Möglichkeit gefunden, in das aktuelle Design einzuarbeiten.
????️ Endformat & Übergabe:
Bitte das fertige Layout als .afdesign Datei (Affinity Designer) liefern
Optional PSD, EPS

```html
<!DOCTYPE html>
<html lang="de">
<head>
<meta charset="utf-8">
<title>Ritmo y Alma – Tanzschule Schild</title>
<link rel="stylesheet" href="https://fonts.googleapis.com/css2?family=Montserrat:wght@400;500;700;800&display=swap">
<style>
  :root {
    --page-bg: #b4b4b4;
    --crimson: #ad194f;
    --crimson-light: #c21d58;
    --gold: #9c7b4f;
    --gold-light: #b8966a;
    --slate: #5f7c86;
    --white: #ffffff;
    --ink: #2b2b2b;
  }
  html, body {
    margin: 0;
    padding: 0;
    width: 923px;
    height: 1200px;
    overflow: hidden;
    background: var(--page-bg);
    font-family: "Montserrat", sans-serif;
  }
  .sign {
    position: absolute;
    left: 56px;
    top: 397px;
    width: 810px;
    height: 405px;
    background: var(--white);
    box-shadow: 0 10px 24px rgba(0,0,0,0.25);
    overflow: hidden;
  }
  .sign-shapes {
    position: absolute;
    inset: 0;
  }
  .eyebrow {
    position: absolute;
    left: 58px;
    top: 42px;
    margin: 0;
    color: var(--white);
    font-size: 17px;
    font-weight: 500;
    letter-spacing: 13.5px;
  }
  .dance-styles {
    position: absolute;
    left: 56px;
    top: 70px;
    margin: 0;
    padding: 0;
    list-style: none;
    color: var(--white);
    font-size: 57px;
    font-weight: 800;
    line-height: 55px;
    letter-spacing: -0.5px;
  }
  .cta {
    position: absolute;
    left: 53px;
    top: 310px;
    width: 290px;
    height: 34px;
    box-sizing: border-box;
    border: 2px solid var(--white);
    border-radius: 18px;
    background: linear-gradient(180deg, var(--gold-light), var(--gold));
    box-shadow: 0 3px 6px rgba(0,0,0,0.3);
    color: var(--white);
    font-size: 16.5px;
    font-weight: 800;
    letter-spacing: -0.2px;
    display: flex;
    align-items: center;
    justify-content: center;
  }
  .website {
    position: absolute;
    left: 53px;
    top: 351px;
    display: flex;
    align-items: center;
    gap: 8px;
    color: var(--white);
    font-size: 22px;
    font-weight: 400;
    letter-spacing: -0.2px;
  }
  .website strong { font-weight: 700; }
  .brand {
    position: absolute;
    left: 455px;
    top: 328px;
    display: flex;
    align-items: center;
    gap: 14px;
  }
  .brand-name {
    color: var(--ink);
    font-size: 32px;
    font-weight: 500;
  }
  .brand-dot {
    width: 28px;
    height: 28px;
    border-radius: 50%;
    background: var(--crimson);
  }
</style>
</head>
<body>
  <section class="sign">
    <svg class="sign-shapes" viewBox="0 0 810 405" width="810" height="405" aria-hidden="true">
      <defs>
        <linearGradient id="crimsonFill" x1="0" y1="0" x2="1" y2="0">
          <stop offset="0" stop-color="#ad194f"/>
          <stop offset="0.75" stop-color="#ad194f"/>
          <stop offset="1" stop-color="#c21d58"/>
        </linearGradient>
        <linearGradient id="goldFill" x1="0" y1="0" x2="0" y2="1">
          <stop offset="0" stop-color="#9c7b4f"/>
          <stop offset="0.5" stop-color="#b8966a"/>
          <stop offset="1" stop-color="#8c6d44"/>
        </linearGradient>
        <linearGradient id="photoFill" x1="0" y1="0.1" x2="1" y2="0.3">
          <stop offset="0" stop-color="#57575c"/>
          <stop offset="0.2" stop-color="#6a6866"/>
          <stop offset="0.32" stop-color="#b0915f"/>
          <stop offset="0.44" stop-color="#d8c2a8"/>
          <stop offset="0.52" stop-color="#e6e2de"/>
          <stop offset="0.64" stop-color="#c9a58a"/>
          <stop offset="0.76" stop-color="#4e7463"/>
          <stop offset="0.88" stop-color="#587a66"/>
          <stop offset="1" stop-color="#5a5a60"/>
        </linearGradient>
      </defs>
      <rect class="photo-area" x="340" y="0" width="470" height="298" fill="url(#photoFill)" role="img" aria-label="Foto eines lachenden Tanzpaares in Salsa-Pose vor grauem Studiohintergrund: Frau mit wehendem blondem Haar im weißen Top, Mann im grünen T-Shirt"/>
      <path class="band-slate" d="M0,0 H348 C445,90 462,272 385,405 H0Z" fill="#5f7c86"/>
      <path class="band-white" d="M0,0 H343 C436,90 452,272 373,405 H0Z" fill="#ffffff"/>
      <path class="band-gold" d="M0,0 H337 C428,90 442,272 362,405 H0Z" fill="url(#goldFill)"/>
      <path class="band-white-inner" d="M0,0 H326 C415,90 428,272 350,405 H0Z" fill="#ffffff"/>
      <path class="panel-crimson" d="M0,0 H321 C410,90 423,272 345,405 H0Z" fill="url(#crimsonFill)"/>
    </svg>

    <p class="eyebrow">TANZSCHULE</p>
    <ul class="dance-styles">
      <li>SALSA</li>
      <li>BACHATA</li>
      <li>KIZOMBA</li>
      <li>ZOUK</li>
    </ul>
    <div class="cta">JETZT GRATIS SCHNUPPERN!</div>
    <div class="website">
      <svg width="13" height="13" viewBox="0 0 13 13" aria-hidden="true">
        <circle cx="6.5" cy="6.5" r="6.5" fill="#ffffff"/>
        <g fill="none" stroke="#ad194f" stroke-width="0.9">
          <circle cx="6.5" cy="6.5" r="4"/>
          <ellipse cx="6.5" cy="6.5" rx="1.8" ry="4"/>
          <line x1="2.5" y1="6.5" x2="10.5" y2="6.5"/>
        </g>
      </svg>
      <span>www.<strong>ritmo-y-alma</strong>.de</span>
    </div>

    <div class="brand">
      <span class="brand-name">Ritmo y Alma</span>
      <span class="brand-dot"></span>
    </div>
  </section>
</body>
</html>
```